We are launching in December, a range of supplements and vitamins.

We have just made an amend to the mission statement and how we are going to give back to society. Please can you add both to the packaging:

Verdant’s purpose is to support health, wellbeing and longevity, so that we can all thrive in the modern world; an environment so alien to that in which we evolved. Embracing technology, research and science, we harness nature’s goodness - enabling us all to love life – naturally.

Twice Kind Promise. For each and every Verdant supplement you take, we provide a supplement to an under nourished child.

For every supplement we sell: £1 goes to the charity ‘Little Lights Fund’ and in addition we provide one healthy meal to an under privileged child in India.

My name is Mark Holloway and I own several companies including www.quartzelle.com (you can check me out on Infopedex – I am not the football referee nor the rocket scientist, but the entrepreneur) . Over the past 2 years I have been writing a book to help people live more healthily and it launches in December. It’s called Verdant Way. While doing my research for the book, I came to realise that most supplements and vitamin products on the market are rubbish! Most are made for profit and not for the benefit of the consumer. I want to change all of that. Howard Pellow is patron of a charity I set up with my brother Paul Holloway and together we have built 11 schools in Asia. I am hoping to get Howards help in getting my supplements to market.

Positioning of our supplements - In a world where so much has changed from the one our bodies were designed to thrive, at Verdant Supplements we are driven by one purpose; to globally provide healthy support to life in the 21st century. While the roots of our wellbeing supplements date back beyond 10,000BC, we embrace modern technology and science, to encapsulate powerful phytonutrients, herbs and other goodness. The essence of which is to promote health, happiness and longevity.

So what are we looking for in the design? Something that stands out. Something that looks professional. A design and concept that can role out across 24 different products. Some products are simple, just one ingredient, such as vitamin D3, Magnesium, Garlic Extracts etc, and others are our own formulas where there are up to 30 different ingredients. You can contact me at any time with questions at Mark@verdantway-example.com

Target Market(s)

Male & Female 20 years plus, mainly UK

Industry/Entity Type

Medical

Logo Text

VERDANT - Sub heading = Thriving Days Gently

Colors

Designer to choose colors to be used in the design.

Requirements
Must have
• see attached powerpoint.
• We have just made an amend to the mission statement and how we are going to give back to society. Please can you add both to the packaging:
• Verdant’s purpose is to support health, wellbeing and longevity, so that we can all thrive in the modern world; an environment so alien to that in which we evolved. Embracing technology, research and science, we harness nature’s goodness - enabling us all to love life – naturally.
• Twice Kind Promise. For each and every Verdant supplement you take, we provide a supplement to an under nourished child.
Nice to have
• see attached powerpoint
Should not have
• see attached powerpoint

```html
<!DOCTYPE html>
<html lang="en">
<head>
<meta charset="utf-8">
<title>Verdant Supplement – Carton Dieline</title>
<link href="https://fonts.googleapis.com/css2?family=Montserrat:wght@800;900&family=Oswald:wght@600;700&family=Open+Sans:ital,wght@0,400;0,600;0,700;1,700&display=swap" rel="stylesheet">
<style>
  :root{
    --teal-dark:#1f6a6d;
    --teal:#2a8c8a;
    --teal-bright:#2fa89c;
    --teal-light:#a8d6d1;
    --teal-pale:#d3ece8;
    --green-text:#9fe0b0;
    --ink:#1b1b1b;
    --grey:#c9cccd;
    --gold:#e9b526;
    --line:#6d6d6d;
    --white:#ffffff;
  }
  *{box-sizing:border-box;margin:0;padding:0}
  html,body{width:1175px;height:1200px;overflow:hidden;background:var(--white)}
  body{font-family:"Open Sans",Arial,sans-serif;color:var(--ink)}
  .canvas{position:relative;width:1175px;height:1200px;overflow:hidden}
  .dieline{position:absolute;inset:0;pointer-events:none}
  .panel{position:absolute;overflow:hidden}

  /* ---------- brand lockups ---------- */
  .brand-word{font-family:"Montserrat",Arial,sans-serif;font-weight:900;color:var(--ink);line-height:1;letter-spacing:0;white-space:nowrap}
  .brand-sub{font-family:"Montserrat",Arial,sans-serif;font-weight:800;color:var(--teal);line-height:1;letter-spacing:1px;white-space:nowrap}
  .tagline-pill{display:inline-block;background:var(--teal-bright);color:var(--white);font-family:"Montserrat",Arial,sans-serif;font-weight:800;border-radius:6px;letter-spacing:1px;line-height:1;white-space:nowrap}
  .headline{font-family:"Oswald",Arial,sans-serif;font-weight:700;color:var(--ink);line-height:1;text-transform:uppercase;white-space:nowrap}
  .brand-dot{display:inline-block;border-radius:50%;background:var(--teal-bright);border:3px solid var(--white);flex:none}

  /* ---------- lid ---------- */
  .lid{left:150px;top:70px;width:730px;height:240px;background:var(--white)}
  .lid-info{position:absolute;left:0;top:0;width:330px;height:240px;background:var(--teal-dark);color:var(--white);padding:16px 22px}
  .lid-info h3{font-size:9.5px;font-weight:700;margin-bottom:3px}
  .lid-info p{font-size:8px;line-height:1.35}
  .lid-info .mission{margin-top:8px;font-size:7.4px;line-height:1.3}
  .lid-info .mission b{font-size:8px}
  .lid-front{position:absolute;left:330px;top:0;width:400px;height:240px;text-align:center}
  .lid-front .brand-dot{position:absolute;left:182px;top:14px;width:36px;height:36px}
  .lid-front .brand-word{position:absolute;left:0;right:0;top:58px;font-size:46px}
  .lid-front .brand-sub{position:absolute;left:0;right:0;top:104px;font-size:23px}
  .lid-front .tagline-pill{position:absolute;left:128px;top:130px;width:144px;font-size:9.5px;padding:3px 0}
  .lid-front .headline{position:absolute;left:0;right:0;top:148px;font-size:26px}
  .lid-front .claims{position:absolute;left:0;right:0;top:180px;font-size:7px;font-weight:700}
  .lid-front .promise{position:absolute;left:118px;top:200px;width:96px;font-size:6px;line-height:1.2;color:var(--white);text-align:left}
  .lid-front .seal{position:absolute;left:280px;top:200px;width:24px;height:24px;border-radius:50%;background:var(--gold)}

  /* ---------- back panel ---------- */
  .back{left:150px;top:510px;width:326px;height:550px;background:var(--white)}
  .back-header{position:absolute;left:0;top:0;width:100%;height:94px;background:var(--teal-dark);padding:20px 0 0 42px}
  .back-header .brand-row{display:flex;align-items:center;gap:10px}
  .back-header .brand-dot{width:34px;height:34px}
  .back-header .brand-word{color:var(--white);font-size:26px}
  .back-header .brand-sub{color:var(--white);font-size:13px;margin-top:2px}
  .back-header .est{color:var(--white);font-size:12px;font-weight:600;margin:8px 0 0 44px}
  .back-header .est sup{font-size:7px}
  .back-nutrition{position:absolute;left:0;top:94px;width:100%;height:156px;padding:12px 14px 0 30px;background:linear-gradient(180deg,#f2f2f2 0,var(--white) 12px)}
  .back-nutrition h3{font-size:11px;font-weight:700;margin-bottom:3px}
  .back-nutrition p{font-size:8.7px;line-height:1.3}
  .back-why{position:absolute;left:0;top:250px;width:100%;height:150px;background:var(--teal-pale);padding:10px 12px 0 8px}
  .back-why .portrait{position:absolute;left:14px;top:14px;width:68px;height:92px;background:linear-gradient(180deg,#d9e7e5,#7d9290);border-radius:3px}
  .back-why h4{margin-left:80px;font-size:13px;font-weight:700;font-style:italic}
  .back-why p{font-size:9.6px;line-height:1.36}
  .back-why p .lead{display:block;margin-left:80px}
  .back-give{position:absolute;left:0;top:400px;width:100%;height:112px;background:var(--teal-dark);padding:9px 14px;color:var(--white);text-align:center}
  .back-give .charity{font-size:11.2px;font-weight:700;font-style:italic;line-height:1.3}
  .back-give .kind{margin-top:5px;font-size:9.4px;line-height:1.3}
  .back-footer{position:absolute;left:0;top:512px;width:100%;height:38px;display:flex;align-items:center;padding-left:30px;gap:22px}
  .back-footer .origin-mark{width:34px;height:22px;background:var(--teal-light);flex:none}
  .back-footer .web{font-size:10px;font-weight:700;white-space:nowrap}

  /* ---------- side panels ---------- */
  .side{top:510px;width:104px;height:550px;background:var(--teal-light)}
  .side-left{left:476px}
  .side-right{left:896px}
  .side-lockup{position:absolute;left:0;width:104px;display:flex;align-items:center;gap:14px}
  .side-left .side-lockup{top:40px;flex-direction:column}
  .side-right .side-lockup{bottom:40px;flex-direction:column-reverse}
  .side .brand-dot{width:44px;height:44px}
  .side-text{writing-mode:vertical-rl;display:flex;align-items:flex-start;gap:6px}
  .side-right .side-text{transform:rotate(180deg)}
  .side .brand-word{font-size:44px;color:var(--teal-dark)}
  .side .brand-sub{font-size:20px;color:var(--teal)}

  /* ---------- front panel ---------- */
  .front{left:580px;top:510px;width:316px;height:550px;background:var(--white);text-align:center}
  .front-top{position:absolute;left:0;top:0;width:100%;height:78px;background:var(--teal-dark)}
  .front .brand-dot{position:absolute;left:128px;top:36px;width:60px;height:60px;border-width:5px}
  .front .brand-word{position:absolute;left:0;right:0;top:118px;font-size:52px}
  .front .brand-sub{position:absolute;left:0;right:0;top:176px;font-size:29px}
  .front .tagline-pill{position:absolute;left:52px;top:212px;width:212px;font-size:14px;padding:5px 0}
  .front .headline-1{position:absolute;left:0;right:0;top:242px;font-size:40px}
  .front .headline-2{position:absolute;left:0;right:0;top:286px;font-size:28px}
  .front-base{position:absolute;left:0;top:360px;width:100%;height:190px;background:var(--teal-dark)}
  .front-claims{position:absolute;left:0;right:0;top:396px;color:var(--green-text);font-weight:700;font-size:12.4px;line-height:1.6}
  .front-promise{position:absolute;left:24px;top:476px;width:170px;color:var(--white);font-size:12px;line-height:1.2;text-align:center}
  .front-promise b{font-size:13px}
  .front-seal{position:absolute;left:222px;top:472px;width:60px;height:60px;border-radius:50%;background:radial-gradient(circle,#fff3b0 0 45%,var(--gold) 47%)}
  .swoosh{position:absolute;left:0;width:100%}
</style>
</head>
<body>
<main class="canvas">

  <svg class="dieline" width="1175" height="1200" viewBox="0 0 1175 1200" aria-hidden="true">
    <g fill="none" stroke="var(--line)" stroke-width="1.2">
      <path d="M150 510 V400 Q150 372 178 372 H448 Q476 372 476 400 V510"/>
      <path d="M96 372 H150"/>
      <path d="M476 510 V440 L490 425 H566 L580 440 V510"/>
      <path d="M896 510 V440 L910 425 H986 L1000 440 V510"/>
      <path d="M150 510 H96 V1060 H150"/>
      <path d="M1000 530 L1040 550 V1020 L1000 1040"/>
      <path d="M580 1060 V1120 Q580 1160 620 1160 H856 Q896 1160 896 1120 V1060"/>
      <path d="M150 1060 V1120 L175 1140 H450 L476 1120 V1060"/>
      <path d="M476 1060 V1110 L492 1130 H564 L580 1110 V1060"/>
      <path d="M896 1060 V1110 L912 1130 H984 L1000 1110 V1060"/>
    </g>
  </svg>

  <section class="panel lid">
    <div class="lid-info">
      <h3>NUTRITIONAL INFORMATION PER 1CAPSULE</h3>
      <p>Vitamin C 80mg (100% NRV), Black Soy Bean1000mg (Glycinemax (L.) merr) (seeds) (from 50mg of 20:1 extract), Chitosan 50mg, Apple Cider Vinegar 17.5mg (Standardised to contain1000mg (Phaseolus vulgaris L) (bean) (from 50mg of 20:1 extract), Chromium 40mcg (100% NRV), Vitamin C 80mg (100% NRV), Black SoyBean 1000mg (Glycinemax (L.) merr) (seeds) (from 50mg of 20:1 extract), Chitosan 50mg, Apple Cider Vinegar 17.5mg (Standardised to contain 35% Acetic Acid), White Kidney Bean Extract 1000mg (Phaseolus vulgaris L) (bean) (from 50mg of 20:1 extract), Chromium 40mcg(100% NRV).</p>
      <p class="mission"><b>OUR PURPOSE</b><br>Verdant’s purpose is to support health, wellbeing and longevity, so that we can all thrive in the modern world; an environment so alien to that in which we evolved. Embracing technology, research and science, we harness nature’s goodness – enabling us all to love life – naturally.</p>
    </div>
    <div class="lid-front">
      <svg class="swoosh" style="top:0;height:60px" viewBox="0 0 400 60" preserveAspectRatio="none" aria-hidden="true">
        <path d="M0 0 H400 V30 Q200 -5 0 34 Z" fill="var(--teal-dark)"/>
        <path d="M0 34 Q200 -5 400 30 V38 Q200 6 0 42 Z" fill="var(--grey)"/>
      </svg>
      <span class="brand-dot"></span>
      <div class="brand-word">VERDANT</div>
      <div class="brand-sub">SUPPLEMENT</div>
      <span class="tagline-pill">THRIVING DAYS GENTLY</span>
      <div class="headline">Extracting Natures Greatness</div>
      <div class="claims">NO ADDED COLOURING • NO ADDED SUGAR • NO GLUTEN • BPA FREE</div>
      <svg class="swoosh" style="top:188px;height:52px" viewBox="0 0 400 52" preserveAspectRatio="none" aria-hidden="true">
        <path d="M0 22 Q200 -6 400 14 V52 H0 Z" fill="var(--teal-dark)"/>
        <path d="M0 16 Q200 -12 400 8 V14 Q200 -6 0 22 Z" fill="var(--grey)"/>
      </svg>
      <p class="promise">LOVE THE DIFFERENCE IN 30 DAYS, OR GET <b>100%</b> OF YOUR MONEY BACK</p>
      <span class="seal"></span>
    </div>
  </section>

  <section class="panel back">
    <header class="back-header">
      <div class="brand-row">
        <span class="brand-dot"></span>
        <div>
          <div class="brand-word">VERDANT</div>
          <div class="brand-sub">SUPPLEMENT</div>
        </div>
      </div>
      <div class="est">EST<sup>D</sup> 10,000 BC</div>
    </header>
    <div class="back-nutrition">
      <h3>NUTRITIONAL INFORMATION PER 1CAPSULE</h3>
      <p>Vitamin C 80mg (100% NRV), Black Soy Bean1000mg (Glycinemax (L.) merr) (seeds) (from 50mg of 20:1 extract), Chitosan 50mg, Apple Cider Vinegar 17.5mg (Standardised to contain1000mg (Phaseolus vulgaris L) (bean) (from 50mg of 20:1 extract), Chromium 40mcg (100% NRV), Vitamin C 80mg (100% NRV), Black SoyBean 1000mg (Glycinemax (L.) merr) (seeds) (from 50mg of 20:1 extract), Chitosan 50mg, Apple Cider Vinegar 17.5mg (Standardised to contain 35% Acetic Acid), White Kidney Bean Extract 1000mg (Phaseolus vulgaris L) (bean) (from 50mg of 20:1 extract), Chromium 40mcg(100% NRV).</p>
    </div>
    <div class="back-why">
      <div class="portrait" role="img" aria-label="Photo of the company founder"></div>
      <h4>WHY?</h4>
      <p><span class="lead">In a world where so much has changed from the one our bodies were designed to thrive, at Verdant Supplements we are driven by one global purpose; <b>‘to support health in the 21<sup>st</sup> century’</b>. While the roots of our well being supplements date back</span>centuries, herbs and other natural goodness, the essence of which is to promote health, happiness and longevity.</p>
    </div>
    <div class="back-give">
      <p class="charity">For every supplement we sell: £1 goes to the charity ‘Little Lights Fund’ and in addition we provide one healthy meal to an under privileged child in India</p>
      <p class="kind"><b>Twice Kind Promise.</b> For each and every Verdant supplement you take, we provide a supplement to an under nourished child.</p>
    </div>
    <footer class="back-footer">
      <span class="origin-mark"></span>
      <span class="web">VISIT: WWW.VERDANTSUPPLEMENTS.COM</span>
    </footer>
  </section>

  <section class="panel side side-left">
    <div class="side-lockup">
      <span class="brand-dot"></span>
      <div class="side-text">
        <span class="brand-word">VERDANT</span>
        <span class="brand-sub">SUPPLEMENT</span>
      </div>
    </div>
  </section>

  <section class="panel front">
    <div class="front-top"></div>
    <svg class="swoosh" style="top:60px;height:40px" viewBox="0 0 316 40" preserveAspectRatio="none" aria-hidden="true">
      <path d="M0 0 H316 V18 Q160 -4 0 24 Z" fill="var(--teal-dark)"/>
      <path d="M0 24 Q160 -4 316 18 V26 Q160 6 0 32 Z" fill="var(--grey)"/>
    </svg>
    <span class="brand-dot"></span>
    <div class="brand-word">VERDANT</div>
    <div class="brand-sub">SUPPLEMENT</div>
    <span class="tagline-pill">THRIVING DAYS GENTLY</span>
    <div class="headline headline-1">Extracting</div>
    <div class="headline headline-2">Natures Greatness</div>
    <div class="front-base"></div>
    <svg class="swoosh" style="top:320px;height:60px" viewBox="0 0 316 60" preserveAspectRatio="none" aria-hidden="true">
      <path d="M0 40 Q150 0 316 22 V60 H0 Z" fill="var(--teal-dark)"/>
      <path d="M0 30 Q150 -10 316 12 V22 Q150 0 0 40 Z" fill="var(--grey)"/>
    </svg>
    <div class="front-claims">NO ADDED COLOURING • NO ADDED SUGAR<br>NO GLUTEN • BPA FREE</div>
    <p class="front-promise">LOVE THE DIFFERENCE IN<br><b>30 DAYS</b>, OR GET <b>100%</b><br>OF YOUR MONEY BACK</p>
    <span class="front-seal"></span>
  </section>

  <section class="panel side side-right">
    <div class="side-lockup">
      <span class="brand-dot"></span>
      <div class="side-text">
        <span class="brand-word">VERDANT</span>
        <span class="brand-sub">SUPPLEMENT</span>
      </div>
    </div>
  </section>

</main>
</body>
</html>
```